CV/Resume Design Brochure

I require a brochure design for my partner's CV (curriculum vitae or resume in US).

She is looking for work in the retail fashion sector whilst going to university.

It will be a 4 page brochure. A5 size (148mm x 210mm).

The design needs to be professional, modern and eye catching. In particular the colour scheme needs to stand out.

The contact details for the CV contents will be provided to the winning designer only.

Target Market(s)

The target audience is managers of retail stores, in particular fashion outlets.

Industry/Entity Type

Retail

Font styles to use
Serif

Colors

Designer to choose colors to be used in the design.

Requirements
Must have
• Must be eye catching in terms of design and colour, as the target audience will receive a great deal of CVs/resumes. It must also be professional and simply laid out as most managers will simply glance over it at first.
Should not have
• Complicated, intricate design that makes it look unprofessional. It should not have bland, pale colours.

```html
<!DOCTYPE html>
<html lang="en">
<head>
<meta charset="utf-8">
<title>Elaine Morton – Curriculum Vitae</title>
<link rel="stylesheet" href="https://fonts.googleapis.com/css2?family=Bodoni+Moda:ital,opsz,wght@0,6..96,400;1,6..96,400&display=swap">
<style>
  :root {
    --paper: #ece7e7;
    --ink: #111111;
    --magenta: #ff1aa3;
    --rose: #e8195f;
    --lemon: #e6ec2a;
    --petal: #f7f6ec;
  }
  * { margin: 0; padding: 0; box-sizing: border-box; }
  html, body {
    width: 849px;
    height: 1200px;
    overflow: hidden;
    background: var(--paper);
  }
  .cover {
    position: relative;
    width: 849px;
    height: 1200px;
    background: var(--paper);
    overflow: hidden;
  }
  .cover__name {
    position: absolute;
    top: -8px;
    left: 0;
    width: 849px;
    text-align: center;
    white-space: nowrap;
    font-family: "Bodoni Moda", "Didot", serif;
    font-weight: 400;
    font-size: 150px;
    line-height: 1;
    letter-spacing: -2px;
    color: var(--ink);
    transform: scaleX(0.77);
    transform-origin: 50% 0;
    z-index: 2;
  }
  .cover__subtitle {
    position: absolute;
    top: 121px;
    right: 40px;
    white-space: nowrap;
    font-family: "Bodoni Moda", "Didot", serif;
    font-style: italic;
    font-weight: 400;
    font-size: 43px;
    line-height: 1;
    color: var(--ink);
    z-index: 2;
  }
  .cover__illustration {
    position: absolute;
    top: 172px;
    left: 0;
    width: 849px;
    height: 1028px;
    display: block;
  }
</style>
</head>
<body>
  <main class="cover">
    <h1 class="cover__name">Elaine Morton</h1>
    <p class="cover__subtitle">curriculum vitae</p>

    <svg class="cover__illustration" viewBox="0 0 849 1028" role="img"
         aria-label="Fashion illustration: a slender woman in a magenta dress with a yellow top, her hair a burst of pink, yellow and white flowers, swirls and birds, with hand-lettered words friendly, willing to go extra mile, passionate in fashion and team working; red poppies and black and white blooms along the bottom">
      <defs>
        <radialGradient id="hair-bloom" cx="0.5" cy="0.27" r="0.5">
          <stop offset="0" stop-color="var(--lemon)" stop-opacity="0.55"/>
          <stop offset="0.35" stop-color="var(--magenta)" stop-opacity="0.28"/>
          <stop offset="0.7" stop-color="var(--petal)" stop-opacity="0.6"/>
          <stop offset="1" stop-color="var(--paper)" stop-opacity="0"/>
        </radialGradient>
        <linearGradient id="figure-dress" x1="0" y1="0" x2="0" y2="1">
          <stop offset="0" stop-color="var(--paper)" stop-opacity="0"/>
          <stop offset="0.55" stop-color="var(--paper)" stop-opacity="0"/>
          <stop offset="0.75" stop-color="var(--rose)" stop-opacity="0.45"/>
          <stop offset="1" stop-color="var(--magenta)" stop-opacity="0.85"/>
        </linearGradient>
      </defs>
      <rect width="849" height="1028" fill="url(#hair-bloom)"/>
      <rect width="849" height="1028" fill="url(#figure-dress)"/>
    </svg>
  </main>
</body>
</html>
```